Harrowgate Estates Business Card for Apartment Buildings

Create business cards for resident managers who run apartment buildings. The audience is the public who are searching for apartment rentals, and current residents who live at the apartment building. Key design element will be incorporating the company logo, however, the logo cannot dominate. The building name and manager name are more important than the logo. Current business card design leaves little room for copy, so we may need to reduce the size on the current card to allow for more space for copy.

Target Market(s)

Adults 18-65 years of age, who are looking for an apartment rental, plus current residents who live at our apartment buildings.

Industry/Entity Type

Property Management

Contact Information for Business Card

A major design element will be use of the company logo. Important property and manager contact information must be part of the design. The size of the logo will need to be reduced to make room for building and manager contact copy.

Font styles to use
Sans Serif

Colors
3176b5
000000
959595
ffffff

Requirements
Must have
• 1) Incorporate the company logo.
• 2) Use the company colors (dark blue, black/grey, over white).
• 3) FEATURE THE BUILDING NAME
• 4) FEATURE THE MANAGER NAME
• 5) The company name is less important than BUILDING and MANAGER
• 6) Manager contact information
• **SEE ATTACHED CREATIVE BRIEF**
Nice to have
• 1) Back of card logo watermark
• 2) Ability to write notes on back of carfd
Should not have
• Avoid letting the company logo dominate the card, the building name and manager are more important than the company logo.

```html
<!DOCTYPE html>
<html lang="en">
<head>
<meta charset="utf-8">
<title>Harrowgate Estates Business Card</title>
<link href="https://fonts.googleapis.com/css2?family=Open+Sans:wght@400;600;700&display=swap" rel="stylesheet">
<style>
  :root {
    --brand-blue: #1170ab;
    --ink: #2b2b2b;
    --card: #f0efef;
    --white: #ffffff;
    --backdrop: #e4e2de;
    --watermark: #d6dde5;
  }
  html, body {
    margin: 0;
    width: 1200px;
    height: 900px;
    overflow: hidden;
    background: var(--backdrop);
    font-family: "Open Sans", sans-serif;
  }
  .card {
    position: absolute;
    width: 580px;
    height: 358px;
    background: var(--card);
    overflow: hidden;
    box-shadow: 2px 3px 6px rgba(0,0,0,0.35);
  }
  .card--front { left: 320px; top: 87px; }
  .card--back  { left: 320px; top: 478px; width: 583px; }
  .card__arc { position: absolute; inset: 0; }
  .company-name {
    position: absolute;
    left: 34px;
    top: 150px;
    margin: 0;
    color: var(--brand-blue);
    font-weight: 700;
    font-size: 25px;
    line-height: 1.1;
    letter-spacing: 1px;
  }
  .contact {
    position: absolute;
    right: 30px;
    top: 98px;
    text-align: right;
    color: var(--white);
  }
  .contact__name { margin: 0; font-size: 22px; font-weight: 600; line-height: 1.2; }
  .contact__title { margin: 2px 0 28px; font-size: 15px; line-height: 1.2; }
  .contact__list { list-style: none; margin: 0; padding: 0; }
  .contact__item {
    display: flex; justify-content: flex-end; align-items: center; gap: 5px;
    font-size: 16px; line-height: 24.5px; margin-right: -0px;
  }
  .contact__icon { width: 15px; height: 15px; fill: var(--white); }
  .contact__address { margin: 17px 0 0; font-size: 15px; line-height: 22px; }
  .watermark {
    position: absolute;
    left: 0; right: 0; top: 158px;
    text-align: center;
    color: var(--watermark);
    font-weight: 700;
    margin: 0;
  }
  .watermark__main { display: block; font-size: 46px; line-height: 1; letter-spacing: 1px; }
  .watermark__sub { display: block; font-size: 22px; letter-spacing: 6px; margin-top: 4px; }
</style>
</head>
<body>
  <section class="card card--front">
    <svg class="card__arc" width="580" height="358" viewBox="0 0 580 358" aria-hidden="true">
      <circle cx="536" cy="336" r="336" fill="none" stroke="var(--ink)" stroke-width="5"/>
      <circle cx="540" cy="336" r="330" fill="var(--card)"/>
      <circle cx="542" cy="338" r="326" fill="var(--brand-blue)"/>
    </svg>
    <p class="company-name">HARROWGATE<br>ESTATES</p>
    <div class="contact">
      <h1 class="contact__name">DANIEL WHITFIELD</h1>
      <p class="contact__title">PROPERTY MANAGE</p>
      <ul class="contact__list">
        <li class="contact__item">555-210-4418
          <svg class="contact__icon" viewBox="0 0 16 16"><path d="M2 6c0-2 3-3 6-3s6 1 6 3v1h-3V6H5v1H2z M4 8h8l1 5H3z"/></svg></li>
        <li class="contact__item">555-210-4419
          <svg class="contact__icon" viewBox="0 0 16 16"><path d="M4 1h6l2 2v3h2v9H2V6h2z M5 2v4h6V4H9V2z M4 9h2v1H4z M7 9h2v1H7z M10 9h2v1h-2z M4 11h2v1H4z M7 11h2v1H7z M10 11h2v1h-2z"/></svg></li>
        <li class="contact__item">daniel@harrowgateestates.us
          <svg class="contact__icon" viewBox="0 0 16 16"><path d="M1 3h14v10H1z" /><path d="M1.5 3.5 8 9l6.5-5.5" fill="none" stroke="var(--brand-blue)" stroke-width="1.2"/></svg></li>
        <li class="contact__item">www.harrowgateestates.us
          <svg class="contact__icon" viewBox="0 0 16 16"><circle cx="8" cy="8" r="7"/><path d="M5 4c2 1 1 3 3 3s1 3 3 3M9 12c-1-1-3 0-3-2" fill="none" stroke="var(--brand-blue)" stroke-width="1.2"/></svg></li>
      </ul>
      <p class="contact__address">2750 Larkspur Valley Road #B210<br>Fairview, Ca 90415</p>
    </div>
  </section>

  <section class="card card--back">
    <p class="watermark">
      <span class="watermark__main">HARROWGATE</span>
      <span class="watermark__sub">ESTATES</span>
    </p>
  </section>
</body>
</html>
```